Kestrel Wiring - Electrician company flyers for new clients

I want a flyer that will be dropped into mailboxes and will hopefully stand out more that the ones i have tried to mock up. I have attached my latest design to give you an idea but it is rather boring.

The aim is obviously to entice new customers into calling me for any electrical work, mainly domestic but i also do commercial work.
I will also upload a photo of my business card so that it can be used as a reference and my website is www.kestrelwiring.co.nz for any extra information.

Ideally the flyer will be DL size
measurements from printmorrow is that's any help
Document Trim Size
99 x 210 mm
1169 x 2480 pixels
Full Bleed Size
102 x 213 mm
1205 x 2516 pixels

Target Market(s)

Domestic electrical works

Industry/Entity Type

Electrician

Requirements
Must have
• all of my contact details -
• Dean Forsyth
• Dean@kestrelwiring.co.nz
• 027 3815 942
• www.kestrelwiring.co.nz
• A little write up similar to the one written on my draft but there's probably alot of room for improvement as my writing skills are lacking.
Nice to have
• clear and concise writing so that people wont throw it away before reading

```html
<!DOCTYPE html>
<html lang="en">
<head>
<meta charset="utf-8">
<title>Kestrel Wiring – DL Flyer</title>
<link href="https://fonts.googleapis.com/css2?family=Archivo+Black&family=Open+Sans:wght@400;600&display=swap" rel="stylesheet">
<style>
  :root {
    --backdrop: #d6d6d6;
    --paper: #ffffff;
    --brand-blue: #0aa2e4;
    --headline-blue: #37a1d3;
    --band-blue: #0b8fd0;
    --slate: #808080;
    --ink: #151515;
    --white: #ffffff;
  }
  * { margin: 0; padding: 0; box-sizing: border-box; }
  html, body {
    width: 1200px; height: 1200px; overflow: hidden;
    background: var(--backdrop);
  }
  .flyer {
    position: absolute; left: 327px; top: 30px;
    width: 546px; height: 1140px;
    background: var(--paper);
    overflow: hidden;
    font-family: "Open Sans", Arial, sans-serif;
  }
  .brand {
    position: absolute; left: 0; top: 30px; width: 100%;
    text-align: center;
    font-family: "Archivo Black", "Arial Black", sans-serif;
    color: var(--brand-blue);
    line-height: 1;
  }
  .brand__name { display: block; font-size: 78px; letter-spacing: 1px; }
  .brand__trade { display: block; font-size: 40px; letter-spacing: 14px; margin-top: 10px; padding-left: 14px; }

  .hero-photo {
    position: absolute; left: 0; top: 184px; width: 434px; height: 277px;
    background: linear-gradient(180deg, #a9cbe8 0%, #dfe9f1 45%, #b9c2c9 70%, #3fa7a8 100%);
  }
  .headline {
    position: absolute; left: 202px; top: 228px; width: 344px; height: 193px;
    background: var(--headline-blue);
    padding: 15px 0 0 17px;
    font-family: "Archivo Black", "Arial Black", sans-serif;
    color: var(--white);
    font-size: 36px; line-height: 41.6px;
    text-transform: uppercase;
  }

  .intro {
    position: absolute; left: 26px; top: 482px; width: 500px;
    border-left: 9px solid var(--brand-blue);
    padding-left: 13px;
    font-size: 23.5px; line-height: 27.2px; color: var(--ink);
    height: 162px;
  }
  .intro p { margin-top: -6px; }

  .local {
    position: absolute; left: 0; top: 659px; width: 100%; height: 345px;
    background: var(--slate);
  }
  .local__text {
    position: absolute; left: 26px; top: 6px; width: 494px;
    color: var(--white); font-size: 19px; line-height: 22.7px;
    text-align: justify; letter-spacing: 0.3px;
  }
  .work-photo {
    position: absolute; left: 26px; top: 87px; width: 493px; height: 248px;
    border: 5px solid var(--white);
    background: linear-gradient(100deg, #2c4f86 0%, #6d7b8c 35%, #c9ccce 65%, #e5e6e6 100%);
  }

  .contact {
    position: absolute; left: 0; top: 1004px; width: 100%; height: 136px;
    background: var(--band-blue); color: var(--white);
  }
  .contact__title {
    position: absolute; left: 0; top: 10px; width: 100%;
    text-align: center; font-weight: 600; font-size: 27px; line-height: 34px;
  }
  .contact__rule {
    position: absolute; top: 26px; height: 3px; width: 109px; background: var(--white);
  }
  .contact__rule--left { left: 35px; }
  .contact__rule--right { left: 403px; }
  .contact__item {
    position: absolute; display: flex; align-items: center; gap: 8px;
    white-space: nowrap;
  }
  .contact__name { left: 26px; top: 50px; font-size: 23.5px; font-weight: 600; }
  .contact__phone { left: 290px; top: 50px; font-size: 23.5px; font-weight: 600; }
  .contact__email { left: 28px; top: 83px; font-size: 17px; }
  .contact__web { left: 290px; top: 83px; font-size: 17px; }
  .contact svg { fill: var(--white); flex: none; }
</style>
</head>
<body>
  <main class="flyer">
    <header class="brand">
      <span class="brand__name">KESTREL</span>
      <span class="brand__trade">WIRING</span>
    </header>

    <div class="hero-photo" role="img" aria-label="Photo of a city harbour bridge and waterfront towers under a blue sky"></div>
    <h1 class="headline">Do you need<br>a local and<br>reliable<br>electrician?</h1>

    <section class="intro">
      <p>Specializing in residential and commercial electrical services, we are dedicated to providing customer service that is second to none. Whether you need a small wiring fix or the full installation , we can get the job done right.</p>
    </section>

    <section class="local">
      <p class="local__text">Based in Kowhai Bay, We are your local Electricians with our main aim to keep our work and communica-tion to a very high standard.</p>
      <div class="work-photo" role="img" aria-label="Photo of an electrician in a hard hat working on a switchboard"></div>
    </section>

    <footer class="contact">
      <span class="contact__rule contact__rule--left"></span>
      <h2 class="contact__title">Contact us today</h2>
      <span class="contact__rule contact__rule--right"></span>

      <div class="contact__item contact__name">Dean Forsyth</div>
      <div class="contact__item contact__phone">
        <svg width="18" height="18" viewBox="0 0 24 24" aria-hidden="true"><path d="M6.6 10.8c1.4 2.8 3.8 5.1 6.6 6.6l2.2-2.2c.3-.3.7-.4 1-.2 1.1.4 2.3.6 3.6.6.6 0 1 .4 1 1V20c0 .6-.4 1-1 1C10.6 21 3 13.4 3 4c0-.6.4-1 1-1h3.5c.6 0 1 .4 1 1 0 1.3.2 2.5.6 3.6.1.3 0 .7-.2 1z"/></svg>
        027 3815 942
      </div>
      <div class="contact__item contact__email">
        <svg width="16" height="12" viewBox="0 0 16 12" aria-hidden="true"><path d="M0 0h16v12H0z M1.5 1.5 8 6.5l6.5-5" fill="none" stroke="#fff" stroke-width="1.6"/><rect x="0" y="0" width="16" height="12" fill="#fff" opacity="0.001"/><path d="M0 0h16L8 6z"/><path d="M0 1.5v10.5h16V1.5L8 7.5z"/></svg>
        Dean@kestrelwiring.co.nz
      </div>
      <div class="contact__item contact__web">
        <svg width="18" height="18" viewBox="0 0 24 24" aria-hidden="true"><circle cx="12" cy="12" r="9.5" fill="none" stroke="#fff" stroke-width="2"/><ellipse cx="12" cy="12" rx="4.2" ry="9.5" fill="none" stroke="#fff" stroke-width="1.8"/><path d="M2.5 12h19M4 7h16M4 17h16" stroke="#fff" stroke-width="1.6"/></svg>
        www.kestrelwiring.co.nz
      </div>
    </footer>
  </main>
</body>
</html>
```